Tall Harbor Business Card

We are a Video Production and Video Equipment Rental company specialising in the supply of state of the art Video Technology and Services for the Live Entertainment, Television and Corporate Business Theatre markets. (in Sydney, Australia) www.tallharbor-media.example

Industry/Entity Type

Business

Contact Information for Business Card

name, position, email, website, address, logo
Example attached of the information we need - doesn't necessarily have to look the same

Font styles to use
Other font styles liked:
• Tall Harbor logo font is GOTHAM

Colors
ea1f27

Requirements
Nice to have
• either matt black or shiny black cards -
raised logo

```html
<!DOCTYPE html>
<html lang="en">
<head>
<meta charset="utf-8">
<title>Tall Harbor Business Card</title>
<link href="https://fonts.googleapis.com/css2?family=Montserrat:wght@500&family=Open+Sans:wght@400;600&display=swap" rel="stylesheet">
<style>
  :root {
    --page: #d9d9d9;
    --card: #333335;
    --red: #e63a43;
    --white: #f2f2f2;
    --divider: #1e1e1f;
  }
  * { box-sizing: border-box; margin: 0; padding: 0; }
  html, body { width: 1200px; height: 1200px; overflow: hidden; background: var(--page); }
  .canvas { position: relative; width: 1200px; height: 1200px; }
  .card {
    position: absolute; left: 220px; width: 760px; height: 434px;
    background: var(--card); overflow: hidden;
    box-shadow: 0 6px 18px rgba(0,0,0,.25);
  }
  .card--front { top: 120px; }
  .card--back { top: 640px; }

  .front-band { position: absolute; top: 0; bottom: 0; width: 64px; background: var(--red); }
  .front-band--left { left: 0; }
  .front-band--right { right: 0; }
  .front-name {
    position: absolute; inset: 0; display: flex; align-items: center; justify-content: center;
    font-family: "Montserrat", sans-serif; font-weight: 500; font-size: 58px;
    letter-spacing: 2px; color: var(--white);
  }

  .back-name {
    position: absolute; left: 52px; top: 150px; width: 330px; text-align: center;
    font-family: "Montserrat", sans-serif; font-weight: 500; font-size: 36px;
    letter-spacing: 1px; color: var(--white);
  }
  .divider { position: absolute; left: 395px; top: 40px; width: 3px; height: 260px; background: var(--divider); }
  .services {
    position: absolute; left: 0; right: 0; bottom: 46px; text-align: center;
    font-family: "Open Sans", sans-serif; font-size: 15px; letter-spacing: .5px; color: var(--white);
  }
  .person { position: absolute; left: 420px; top: 58px; font-family: "Open Sans", sans-serif; }
  .person-name { font-size: 26px; font-weight: 600; color: var(--red); letter-spacing: 1px; }
  .person-title { font-size: 16px; font-weight: 600; color: var(--white); margin-top: 2px; }
  .contact { position: absolute; left: 372px; top: 150px; font-family: "Open Sans", sans-serif; }
  .contact-row { display: flex; align-items: flex-start; gap: 18px; height: 36px; }
  .contact-icon { width: 30px; height: 26px; background: var(--red); display: flex; align-items: center; justify-content: center; flex: none; }
  .contact-text { font-size: 17px; color: var(--white); line-height: 24px; }
  .contact-text .accent { color: var(--red); }
</style>
</head>
<body>
<main class="canvas">
  <section class="card card--front" aria-label="Card front">
    <div class="front-band front-band--left"></div>
    <div class="front-band front-band--right"></div>
    <div class="front-name">TALL HARBOR</div>
  </section>

  <section class="card card--back" aria-label="Card back">
    <div class="back-name">TALL HARBOR</div>
    <div class="divider"></div>
    <div class="person">
      <div class="person-name">MARA LINWOOD</div>
      <div class="person-title">Managing Director</div>
    </div>
    <div class="contact">
      <div class="contact-row">
        <span class="contact-icon"><svg width="16" height="12" viewBox="0 0 16 12"><rect x="0.5" y="0.5" width="15" height="11" fill="none" stroke="#fff"/><path d="M1 1 L8 7 L15 1" fill="none" stroke="#fff"/></svg></span>
        <span class="contact-text">MARA@<span class="accent">TALLHARBOR-MEDIA</span>.EXAMPLE</span>
      </div>
      <div class="contact-row">
        <span class="contact-icon"><svg width="14" height="14" viewBox="0 0 14 14"><circle cx="7" cy="7" r="6" fill="none" stroke="#fff"/><ellipse cx="7" cy="7" rx="2.6" ry="6" fill="none" stroke="#fff"/><path d="M1 7 H13" stroke="#fff"/></svg></span>
        <span class="contact-text">WWW.<span class="accent">TALLHARBOR-MEDIA</span>.EXAMPLE</span>
      </div>
      <div class="contact-row">
        <span class="contact-icon"><svg width="14" height="13" viewBox="0 0 14 13"><path d="M7 0 L14 6 H12 V13 H8.5 V9 H5.5 V13 H2 V6 H0 Z" fill="#fff"/></svg></span>
        <span class="contact-text">12 QUAY LANE,<br>HARBOURSIDE NSW 2000<br>AUSTRALIA</span>
      </div>
    </div>
    <div class="services">VIDEO SOLUTIONS &nbsp;-&nbsp; LED SCREENS &nbsp;-&nbsp; CAMERA SYSTEMS &nbsp;-&nbsp; PROJECTION</div>
  </section>
</main>
</body>
</html>
```